Frameless shower doors web site

Build a web site for information and display past projects. Contact information, type of work done. Customer Reviews. The design purpose is to generate phone calls and email inquirers. Domain name is Southernshowerdoors.comEmail is Brightpanelworks@mailbarn.com Profile We Love What We Do!Lakeview Bath Panels & Mirror LLC. is committed to excellence in every aspect of our business. We hold a standard of integrity bound by fairness, honesty, and personal responsibility. Our distinction is the quality of service and attention to detail we bring to each project. Above all, we listen to our clients input to provide several design options available from designer glass to hardware. We also service and repair existing shower and tub enclosure. Installation of customer purchased enclosure are available by appointment. and address any concerns.

Target Market(s)

25 to 55 residential customers

Number of Pages Required

4 page

Font styles to use
Sans Serif

Colors

Designer to choose colors to be used in the design.

Requirements
Nice to have
• Looking to drive phone calls for estimating shower projects
Should not have
• Lot of prescriptive words, Clutter

```html
<!DOCTYPE html>
<html lang="en">
<head>
<meta charset="utf-8">
<title>Lakeview Bath Panels – Website Design</title>
<link href="https://fonts.googleapis.com/css2?family=Montserrat:wght@300;400;500;600;700&display=swap" rel="stylesheet">
<style>
:root{
  --stage:#ececec;
  --navy:#1f3a78;
  --navy-deep:#1c3571;
  --blue:#1679bf;
  --btn:#1e3b78;
  --white:#ffffff;
  --pale:#cfe2f3;
  --footer:#f6f6f6;
  --footer-bar:#ececec;
  --ink:#1f3a78;
  --grey:#8a8a8a;
}
*{margin:0;padding:0;box-sizing:border-box}
html,body{width:1200px;height:1200px;overflow:hidden}
body{background:var(--stage);font-family:'Montserrat',sans-serif;position:relative;color:var(--white)}
.page{position:absolute;width:560px;overflow:hidden;box-shadow:0 4px 18px rgba(0,0,0,.12)}
.page-home{left:28px;top:112px;height:1088px;background:var(--blue)}
.page-gallery{left:619px;top:0;height:1095px;background:var(--blue)}
.abs{position:absolute}

/* header */
.site-header{left:0;top:0;width:560px;height:46px;background:var(--white)}
.brand{left:82px;top:16px;font-size:13px;font-weight:600;color:var(--navy);letter-spacing:.5px;display:flex;align-items:center;gap:5px}
.brand-dot{width:8px;height:8px;background:var(--blue)}
.nav a{position:absolute;top:20px;font-size:6.4px;color:#555;text-decoration:none}
.nav .active::after{content:"";position:absolute;left:0;right:0;top:20px;height:2px;background:var(--blue)}
.phone-icon{left:364px;top:17px}
.call-box{left:371px;top:0;width:107px;height:46px;background:var(--navy);padding:12px 0 0 11px}
.call-box small{display:block;font-size:7px;color:var(--pale)}
.call-box strong{display:block;font-size:10.5px;font-weight:700;margin-top:2px}

/* hero */
.hero{left:0;top:46px;width:560px;height:252px;background:linear-gradient(90deg,#4a4a4a,#8d8d8d 30%,#6a6a6a 55%,#9a9a9a 80%,#555)}
.hero-title{left:0;top:70px;width:560px;text-align:center;font-size:19px;font-weight:700;line-height:23px}
.hero-sub{left:0;top:145px;width:560px;text-align:center;font-size:17px;font-weight:300;color:#e8e8e8}
.hero-btn{left:217px;top:164px;width:125px;height:30px;background:var(--blue);font-size:8.5px;font-weight:600;display:flex;align-items:center;justify-content:center}

/* about */
.about{left:0;top:298px;width:560px;height:244px;background:var(--navy)}
.section-title{width:560px;left:0;text-align:center;font-size:15px;font-weight:500;letter-spacing:.3px}
.section-title b{font-weight:600}
.about-text{left:143px;top:78px;width:274px;font-size:6.1px;line-height:10.1px;text-align:center}

/* cards */
.card{position:absolute;width:135px}
.photo{width:126px;height:203px}
.card h3{font-size:9.5px;font-weight:600;line-height:11px;margin:15px 0 0 6px}
.card p{font-size:6px;line-height:8.4px;color:var(--pale);margin:5px 0 0 6px;width:118px}
.card .gallery-btn{display:inline-block;margin:9px 0 0 6px;background:var(--btn);font-size:6.2px;letter-spacing:.4px;padding:5px 8px;font-weight:500}
.ph-a{background:linear-gradient(160deg,#e9e9e9,#bdbdbd 60%,#8a7a70)}
.ph-b{background:linear-gradient(160deg,#e3eef4,#b7ccd6 60%,#98a6ad)}
.ph-c{background:linear-gradient(160deg,#d9cba3,#b59a62 55%,#8c7449)}
.ph-d{background:linear-gradient(160deg,#e6ddcf,#c7b69d 55%,#9b8a74)}
.ph-e{background:linear-gradient(160deg,#e4dcd0,#c9b9a2 55%,#a59785)}
.ph-f{background:linear-gradient(160deg,#e9e6de,#cfc6b4 55%,#a9a393)}

/* pagination */
.pager{left:0;top:437px;width:560px;height:26px}
.dot{position:absolute;top:0;width:26px;height:26px;border-radius:50%;background:#6fa6d3;color:#2d5c8f;font-size:8px;display:flex;align-items:center;justify-content:center}
.dot.current{background:var(--white);color:var(--navy);font-weight:700}

/* estimate */
.estimate{left:0;top:505px;width:560px;height:438px;background:var(--navy-deep)}
.contact-line{left:186px}
.contact-line small{display:block;font-size:13px;font-weight:300;color:var(--pale)}
.contact-line strong{display:block;font-size:13.5px;font-weight:700;margin-top:1px}
.direct{left:0;width:560px;text-align:center;font-size:13px;font-weight:400;color:var(--white)}
.direct span{color:var(--pale);font-weight:300}
.field{left:167px;width:226px;height:28px;border:1px solid #3f73b4;font-size:7px;color:#9cbbe0;padding:10px 0 0 12px}

/* footer */
.site-footer{left:0;top:943px;width:560px;height:123px;background:var(--footer);color:var(--ink)}
.foot-col{position:absolute;top:39px;font-size:6.5px}
.foot-col h4{font-size:6.6px;font-weight:700;margin-bottom:8px}
.foot-col li{list-style:none;margin-bottom:8px}
.foot-col .dim{color:#b9b9b9}
.dir-btn{display:inline-block;margin-top:6px;background:var(--blue);color:var(--white);padding:5px 8px;font-size:6px}
.foot-bar{left:0;top:1066px;width:560px;height:29px;background:var(--footer-bar);font-size:5.8px;color:var(--grey)}
.social{position:absolute;top:9px;width:11px;height:11px;border-radius:50%;background:#777}
</style>
</head>
<body>

<!-- Home page -->
<section class="page page-home">
  <header class="abs site-header">
    <div class="abs brand"><span class="brand-dot"></span>LAKEVIEW</div>
    <nav class="nav">
      <a class="active" style="left:179px">Home</a>
      <a style="left:209px">About Us</a>
      <a style="left:249px">Projects</a>
      <a style="left:285px">Gallery</a>
      <a style="left:318px">Contact Us</a>
    </nav>
    <svg class="abs phone-icon" width="12" height="12" viewBox="0 0 24 24"><circle cx="12" cy="12" r="12" fill="#1679bf"/><path d="M8 6l2 0 1 3-1.5 1a7 7 0 0 0 4.5 4.5L15 13l3 1v2c0 1-1 2-2 2A10 10 0 0 1 6 8c0-1 1-2 2-2z" fill="#fff"/></svg>
    <div class="abs call-box"><small>Call for inquiry</small><strong>(555) 014-2288</strong></div>
  </header>

  <div class="abs hero" role="img" aria-label="Black and white photo of frameless glass shower enclosures">
    <div class="abs hero-title">Custom Frameless Shower Doors<br>&amp; Mirrors cut to size</div>
    <div class="abs hero-sub">Free estimates and repairs</div>
    <div class="abs hero-btn">Check our projects</div>
  </div>

  <div class="abs about">
    <h2 class="abs section-title" style="top:37px"><b>ABOUT US</b> AND <b>OUR PROJECTS</b></h2>
    <p class="abs about-text">Lakeview Bath Panels &amp; Mirror LLC. is committed to excellence in every aspect of our business. We hold a standard of integrity bound by fairness, honesty, and personal responsibility. Our distinction is the quality of service and attention to detail we bring to each project. Above all, we listen to our clients input to provide several design options available from designer glass to hardware. We also service and repair existing shower and tub enclosure. Installation of customer purchased enclosure are available by appointment and address any concerns.</p>
  </div>

  <article class="card" style="left:82px;top:477px">
    <div class="photo ph-a" role="img" aria-label="White subway tile shower with glass door"></div>
    <h3>The very amazing clean door system lorem</h3>
    <p>Lorem ipsum dolor sit amet, consectetur adipisicing elit, sed do eiusmod tempor</p>
    <span class="gallery-btn">VIEW IN GALLERY</span>
  </article>
  <article class="card" style="left:217px;top:477px">
    <div class="photo ph-b" role="img" aria-label="Bright frameless glass shower with rain head"></div>
    <h3>Lorem ipsum dolorsit amet consectetur</h3>
    <p>Sed do eiusmod tempor incididun labore et dolore magna aliqua. Ut enim ad minim veniam</p>
    <span class="gallery-btn">VIEW IN GALLERY</span>
  </article>
  <article class="card" style="left:353px;top:477px">
    <div class="photo ph-c" role="img" aria-label="Warm-lit marble shower behind clear glass"></div>
    <h3>Adipisicing elit seddo eiusmod tempor</h3>
    <p>Quis nostrud exercitation ullamco laboris nisi ut aliquip ex ea commodo consequat. Duis aute</p>
    <span class="gallery-btn">VIEW IN GALLERY</span>
  </article>
  <article class="card" style="left:82px;top:796px">
    <div class="photo ph-d" role="img" aria-label="Beige tile shower with glass door"></div>
    <h3>The very amazing clean door system lorem</h3>
    <p>Lorem ipsum dolor sit amet, consectetur adipisicing elit, sed do eiusmod tempor</p>
    <span class="gallery-btn">VIEW IN GALLERY</span>
  </article>
  <article class="card" style="left:217px;top:796px">
    <div class="photo ph-e" role="img" aria-label="Walk-in shower with pebble floor"></div>
    <h3>Lorem ipsum dolorsit amet consectetur</h3>
    <p>Sed do eiusmod tempor incididun labore et dolore magna aliqua. Ut enim ad minim veniam</p>
    <span class="gallery-btn">VIEW IN GALLERY</span>
  </article>
  <article class="card" style="left:353px;top:796px">
    <div class="photo ph-f" role="img" aria-label="Glass shower panel with granite curb"></div>
    <h3>Adipisicing elit seddo eiusmod tempor</h3>
    <p>Quis nostrud exercitation ullamco laboris nisi ut aliquip ex ea commodo consequat. Duis aute</p>
    <span class="gallery-btn">VIEW IN GALLERY</span>
  </article>
</section>

<!-- Gallery / contact page -->
<section class="page page-gallery">
  <article class="card" style="left:82px;top:-282px">
    <div class="photo ph-d" role="img" aria-label="Shower project photo"></div>
    <h3>The very amazing clean door system lorem</h3>
    <p>Lorem ipsum dolor sit amet, consectetur adipisicing elit, sed do eiusmod tempor</p>
    <span class="gallery-btn">VIEW IN GALLERY</span>
  </article>
  <article class="card" style="left:217px;top:-282px">
    <div class="photo ph-e" role="img" aria-label="Shower project photo"></div>
    <h3>Lorem ipsum dolorsit amet consectetur</h3>
    <p>Sed do eiusmod tempor incididun labore et dolore magna aliqua. Ut enim ad minim veniam</p>
    <span class="gallery-btn">VIEW IN GALLERY</span>
  </article>
  <article class="card" style="left:352px;top:-282px">
    <div class="photo ph-f" role="img" aria-label="Shower project photo"></div>
    <h3>Adipisicing elit seddo eiusmod tempor</h3>
    <p>Quis nostrud exercitation ullamco laboris nisi ut aliquip ex ea commodo consequat. Duis aute</p>
    <span class="gallery-btn">VIEW IN GALLERY</span>
  </article>

  <article class="card" style="left:82px;top:102px">
    <div class="photo ph-d" role="img" aria-label="Beige tile shower with glass door"></div>
    <h3>The very amazing clean door system lorem</h3>
    <p>Lorem ipsum dolor sit amet, consectetur adipisicing elit, sed do eiusmod tempor</p>
    <span class="gallery-btn">VIEW IN GALLERY</span>
  </article>
  <article class="card" style="left:217px;top:102px">
    <div class="photo ph-e" role="img" aria-label="Walk-in shower with pebble floor"></div>
    <h3>Lorem ipsum dolorsit amet consectetur</h3>
    <p>Sed do eiusmod tempor incididun labore et dolore magna aliqua. Ut enim ad minim veniam</p>
    <span class="gallery-btn">VIEW IN GALLERY</span>
  </article>
  <article class="card" style="left:352px;top:102px">
    <div class="photo ph-f" role="img" aria-label="Glass shower panel with granite curb"></div>
    <h3>Adipisicing elit seddo eiusmod tempor</h3>
    <p>Quis nostrud exercitation ullamco laboris nisi ut aliquip ex ea commodo consequat. Duis aute</p>
    <span class="gallery-btn">VIEW IN GALLERY</span>
  </article>

  <div class="abs pager">
    <svg class="abs" style="left:183px;top:7px" width="8" height="12" viewBox="0 0 8 12"><path d="M6 1L1 6l5 5" stroke="#cfe2f3" stroke-width="1.6" fill="none"/></svg>
    <span class="dot" style="left:230px">1</span>
    <span class="dot current" style="left:269px">2</span>
    <span class="dot" style="left:308px">3</span>
    <svg class="abs" style="left:370px;top:7px" width="8" height="12" viewBox="0 0 8 12"><path d="M2 1l5 5-5 5" stroke="#cfe2f3" stroke-width="1.6" fill="none"/></svg>
  </div>

  <div class="abs estimate">
    <h2 class="abs section-title" style="top:38px">GET FREE ESTIMATE</h2>
    <svg class="abs" style="left:147px;top:81px" width="24" height="17" viewBox="0 0 24 17"><rect width="24" height="17" fill="#1679bf"/><path d="M0 0l12 9 12-9" stroke="#1c3571" stroke-width="1.5" fill="none"/></svg>
    <div class="abs contact-line" style="top:79px"><small>Send us an email</small><strong>Brightpanelworks@mailbarn.com</strong></div>
    <svg class="abs" style="left:147px;top:129px" width="24" height="24" viewBox="0 0 24 24"><circle cx="12" cy="12" r="12" fill="#1679bf"/><path d="M8 6l2 0 1 3-1.5 1a7 7 0 0 0 4.5 4.5L15 13l3 1v2c0 1-1 2-2 2A10 10 0 0 1 6 8c0-1 1-2 2-2z" fill="#1c3571"/></svg>
    <div class="abs contact-line" style="top:130px"><small>Call us</small><strong>(555) 014-2288</strong></div>
    <div class="abs direct" style="top:201px"><span>or</span> send us a direct message</div>
    <div class="abs field" style="top:234px">Your name*</div>
    <div class="abs field" style="top:269px">Email address*</div>
    <div class="abs field" style="top:304px">Subject</div>
    <div class="abs field" style="top:340px;height:53px">Your message</div>
  </div>

  <footer class="abs site-footer">
    <div class="foot-col" style="left:114px">
      <h4>About LBPM</h4>
      <ul><li>History</li><li>Projects</li><li>Gallery</li></ul>
    </div>
    <div class="foot-col" style="left:215px">
      <h4>Locate Us</h4>
      <div style="font-size:6px;line-height:9px">2870 Harbor Crest Ln. Fairview, TX 75000<br>United States</div>
      <span class="dir-btn">Get directions</span>
    </div>
    <div class="foot-col" style="left:385px;font-size:6px">
      <h4>Business Hours</h4>
      <div style="line-height:11px">MON-FRI: <b style="font-weight:500">8 AM - 5 PM</b><br>SAT: <b style="font-weight:500">9 AM - 3 PM</b><br><span class="dim">SUN: OFF</span></div>
    </div>
  </footer>
  <div class="abs foot-bar">
    <span class="abs" style="left:114px;top:11px">Copyright. LBPM 2019. &nbsp;&nbsp; Terms &amp; Conditions &nbsp;&nbsp; Privacy Policy</span>
    <span class="social" style="left:383px"></span>
    <span class="social" style="left:402px"></span>
    <span class="social" style="left:422px"></span>
    <span class="social" style="left:441px"></span>
  </div>
</section>

</body>
</html>
```